Grand Opening Banner needed for Marvelous Carpets and Home

My website is www.MarvelousCarpetsandHome.com (login with password 'plorka')

A full page banner 1000px X 500px with bright, lively colors and wording that shows an exciting GRAND OPENING celebration throughout the site. Banner needs to convey the following...

Grand Opening Sale
Runs through end of the month
Savings in every department
30 day Returns
Free Rug Pads with every rug
Free shipping.

Banner can be a simple background with graphics and text, or can be a room scene with rugs and furniture, or a grouping of rugs with text.

Some Ideas and Images can be taken from our vendor's websites, such as:

http://tbvendora.com/
http://dosmir.com/dosmir_2015/
http://www.pqmats.com/
http://zaverto.com/
http://shopbelwyn.com/

I also have quite a few room scene images available for use, if you desire.

Target Market(s)

Affluent women who care about stylish decor for their homes

Industry/Entity Type

Home And Garden

Requirements
Must have
• bold, vibrant appearance. Text that can be modified in Photoshop.
Nice to have
• HAND DRAWN, ARTIST STYLE ARTWORK IS GREATLY APPRECIATED.
• flat graphics and text with little to no 3 dimensional (shadow) effect. Font styles should be elegant/luxurious. An organic, scribbled, or painted style is nice in keeping with the handmade products that we sell.
• I am open to changing the color scheme of the website, to match your banner, so don't feel tied down to my existing colors.
Should not have
• nothing too modern or extreme in style.

```html
<!DOCTYPE html>
<html lang="en">
<head>
<meta charset="UTF-8">
<title>Grand Opening Sale</title>
<link href="https://fonts.googleapis.com/css2?family=Poppins:wght@400;600&display=swap" rel="stylesheet">
<style>
  :root {
    --ink: #111111;
    --paper: #ffffff;
    --shade: rgba(20, 14, 10, 0.5);
    --room-warm: #8a5a2e;
    --room-mid: #5b4634;
    --room-dark: #2b2119;
    --room-light: #c9a06a;
  }
  * { margin: 0; padding: 0; box-sizing: border-box; }
  html, body { width: 1200px; height: 600px; overflow: hidden; background: var(--room-dark); }
  .banner {
    position: relative;
    width: 1200px;
    height: 600px;
    overflow: hidden;
    font-family: "Poppins", "Century Gothic", sans-serif;
    color: var(--paper);
  }
  .room-scene {
    position: absolute; inset: 0;
    background:
      radial-gradient(ellipse at 40% 15%, rgba(230, 190, 130, 0.55), transparent 45%),
      linear-gradient(180deg, var(--room-mid) 0%, var(--room-warm) 45%, var(--room-mid) 75%, var(--room-dark) 100%),
      linear-gradient(90deg, var(--room-light) 0%, var(--room-mid) 60%, var(--room-dark) 100%);
    background-blend-mode: normal, multiply, normal;
  }
  .offer-frame {
    position: absolute;
    left: 182px; top: 60px;
    width: 836px; height: 480px;
    border: 4px solid var(--paper);
    background: var(--shade);
  }
  .headline {
    position: absolute;
    left: 222px; top: 88px;
    font-size: 66px;
    font-weight: 600;
    letter-spacing: 1px;
    line-height: 1;
    white-space: nowrap;
  }
  .perk-list {
    position: absolute;
    left: 276px; top: 186px;
    list-style: none;
  }
  .perk {
    display: flex;
    align-items: center;
    height: 46px;
    width: max-content;
    margin-bottom: 13px;
    padding: 2px 13px 0 12px;
    border: 3px solid var(--paper);
    font-size: 29px;
    font-weight: 400;
    letter-spacing: 0.2px;
    line-height: 1;
    white-space: nowrap;
  }
  .perk-arrow { width: 14px; height: 18px; margin-right: 21px; margin-top: -2px; flex: none; }
  .shipping-badge {
    position: absolute;
    left: 463px; top: 450px;
    width: 267px; height: 64px;
    background: var(--paper);
    padding: 5px;
  }
  .shipping-badge span {
    display: flex;
    align-items: center;
    justify-content: center;
    width: 100%; height: 100%;
    padding-top: 2px;
    border: 3px solid var(--ink);
    color: var(--ink);
    font-size: 27px;
    font-weight: 600;
    letter-spacing: 0.3px;
    line-height: 1;
  }
</style>
</head>
<body>
<main class="banner">
  <div class="room-scene" role="img" aria-label="Warmly lit living room with sofas, a dark coffee table, a lamp and a patterned area rug"></div>
  <div class="offer-frame"></div>
  <h1 class="headline">GRAND OPENING SALE</h1>
  <ul class="perk-list">
    <li class="perk"><svg class="perk-arrow" viewBox="0 0 14 18"><path d="M3 2 L11 9 L3 16" fill="none" stroke="#ffffff" stroke-width="3.5"/></svg>RUNS THROUGH END OF THE MONTH</li>
    <li class="perk"><svg class="perk-arrow" viewBox="0 0 14 18"><path d="M3 2 L11 9 L3 16" fill="none" stroke="#ffffff" stroke-width="3.5"/></svg>SAVINGS IN EVERY DEPARTMENT</li>
    <li class="perk"><svg class="perk-arrow" viewBox="0 0 14 18"><path d="M3 2 L11 9 L3 16" fill="none" stroke="#ffffff" stroke-width="3.5"/></svg>30 DAY RETURNS</li>
    <li class="perk"><svg class="perk-arrow" viewBox="0 0 14 18"><path d="M3 2 L11 9 L3 16" fill="none" stroke="#ffffff" stroke-width="3.5"/></svg>FREE RUG PADS WITH EVERY RUG</li>
  </ul>
  <div class="shipping-badge"><span>FREE SHIPPING.</span></div>
</main>
</body>
</html>
```